Beacon Law Stationary - Law Firm

I am looking for a designer who can help me design letterhead and envelopes consistent with our new business cards. Feel free to reach out to me directly at ned@beaconlawgroup.example. Thank you!! Visit beaconlawgroup.example to see our site and the attached files for creative assets.

Target Market(s)

Anyone needing a lawyer

Font styles to use
Other font styles liked:
• Adobe Caslon Pro

Requirements
Must have
• Adobe Caslon Pro font
Full color
Nice to have
• My photo on front along with 2/3 face of camo - see mock up for example of what I have in mind.

American colors - similar to the ones found on my website and gold.

```html
<!DOCTYPE html>
<html lang="en">
<head>
<meta charset="utf-8">
<title>Beacon Law — Envelope Stationery</title>
<link rel="stylesheet" href="https://fonts.googleapis.com/css2?family=Libre+Caslon+Text:wght@400;700&display=swap">
<style>
  :root {
    --backdrop: #eceeef;
    --navy: #021d3e;
    --gold: #a08f55;
    --white: #ffffff;
    --paper-edge: #d9dbde;
  }
  * { box-sizing: border-box; margin: 0; padding: 0; }
  html, body {
    width: 1200px;
    height: 800px;
    overflow: hidden;
    background: var(--backdrop);
    font-family: "Libre Caslon Text", "Times New Roman", serif;
  }
  .canvas {
    position: relative;
    width: 1200px;
    height: 800px;
  }
  .envelope {
    position: absolute;
    width: 780px;
    height: 338px;
    background: var(--navy);
    box-shadow: 0 2px 0 var(--paper-edge), 0 4px 0 var(--white), 0 6px 0 var(--paper-edge), 0 10px 18px rgba(0,0,0,0.12);
    overflow: hidden;
  }
  .envelope--back { left: 210px; top: 36px; }
  .envelope--front { left: 210px; top: 420px; }

  .envelope__flap {
    position: absolute;
    left: 0;
    top: 0;
    width: 780px;
    height: 92px;
  }
  .envelope__flap path { fill: var(--gold); }
  .envelope__tagline {
    position: absolute;
    left: 0;
    top: 28px;
    width: 100%;
    text-align: center;
    color: var(--white);
    font-size: 21px;
    letter-spacing: 0.3px;
  }

  .brand {
    position: absolute;
    left: 64px;
    top: 56px;
    display: flex;
    align-items: center;
    gap: 18px;
  }
  .brand__mark {
    width: 22px;
    height: 22px;
    background: var(--gold);
  }
  .brand__name {
    color: var(--gold);
    font-size: 27px;
    font-weight: 400;
    letter-spacing: 4px;
    line-height: 1.05;
    text-transform: uppercase;
  }

  .return-address {
    position: absolute;
    left: 64px;
    top: 196px;
    color: var(--white);
    font-style: normal;
    font-size: 15px;
    line-height: 1.35;
  }
</style>
</head>
<body>
  <main class="canvas">
    <section class="envelope envelope--back" aria-label="Envelope back">
      <svg class="envelope__flap" viewBox="0 0 780 92" aria-hidden="true">
        <path d="M0 0 H780 V40 Q778 66 748 74 L700 88 Q690 91 676 91 H104 Q90 91 80 88 L32 74 Q2 66 0 40 Z"/>
      </svg>
      <p class="envelope__tagline">Our Promise: Steady Counsel, Clear Results</p>
    </section>

    <section class="envelope envelope--front" aria-label="Envelope front">
      <div class="brand">
        <span class="brand__mark" aria-hidden="true"></span>
        <p class="brand__name">Beacon<br>Law</p>
      </div>
      <address class="return-address">
        48 Harbor Line Ave<br>
        Easton, FL 32999<br>
        (555) 014-2290<br>
        mara@beaconlawgroup.example<br>
        www.beaconlawgroup.example
      </address>
    </section>
  </main>
</body>
</html>
```